Business Card Design Project

We are rebranding an existing automotive collision repair business. The business is called dentworks garage. I have attached logo but I'm not tied to that. I want to leave this wide open.

I want this card to say we are professional, competent, cutting edge. We are focused on customers and use a lot of the latest technology to make the customer experience different. We sign customers in on iPads. Paperwork I signed electronically and updates are sent via text, email, logging on a website or as they wish. I want this innovation and image to come through in our cards

Target Market(s)

60%. Women 40% men. Age 35-60

Industry/Entity Type

Automotive

Requirements
Must have
• The card must have name, title, phone,email, cell, web page

```html
<!DOCTYPE html>
<html lang="en">
<head>
<meta charset="UTF-8">
<title>Dentworks Garage Business Card</title>
<link href="https://fonts.googleapis.com/css2?family=Oswald:wght@500;600&family=Open+Sans:wght@400&display=swap" rel="stylesheet">
<style>
  :root {
    --bg-start: #47494c;
    --bg-end: #2b3a4d;
    --card-white: #f2f2f2;
    --card-stripe: #e9e9e9;
    --band-gray: #dadada;
    --block-gray: #cdcdcd;
    --panel-gray: #c6c6c6;
    --brand-green: #7cc142;
    --ink-dark: #2b2b2b;
    --ink-body: #444444;
  }
  * { margin: 0; padding: 0; box-sizing: border-box; }
  html, body { width: 1200px; height: 1000px; overflow: hidden; }
  body {
    background: linear-gradient(135deg, var(--bg-start) 0%, var(--bg-end) 100%);
    position: relative;
    font-family: "Open Sans", sans-serif;
  }
  .card {
    position: absolute;
    left: 250px;
    width: 700px;
    height: 400px;
    background:
      repeating-linear-gradient(-45deg, var(--card-white) 0 3px, var(--card-stripe) 3px 4px);
    box-shadow: 0 10px 24px rgba(0,0,0,0.35);
    overflow: hidden;
  }
  .card--front { top: 70px; }
  .card--back { top: 530px; }

  .side-band { position: absolute; left: 0; top: 0; width: 50px; height: 100%; background: var(--band-gray); }
  .accent-green { position: absolute; left: 0; top: 222px; width: 92px; height: 30px; background: var(--brand-green); }
  .accent-gray { position: absolute; left: 0; top: 252px; width: 92px; height: 40px; background: var(--block-gray); }
  .corner-block { position: absolute; right: 0; top: 30px; width: 88px; height: 62px; background: var(--band-gray); }
  .green-band { position: absolute; right: 0; top: 196px; width: 310px; height: 26px; background: var(--brand-green); }

  .company-name {
    position: absolute; left: 110px; top: 208px;
    font-family: "Oswald", sans-serif; font-weight: 600;
    font-size: 34px; letter-spacing: 0.5px; color: var(--ink-dark);
    text-transform: uppercase; line-height: 1;
  }
  .person {
    position: absolute; right: 100px; top: 34px; text-align: right;
  }
  .person__name {
    font-family: "Oswald", sans-serif; font-weight: 600;
    font-size: 30px; color: var(--brand-green); line-height: 1; text-transform: uppercase;
  }
  .person__title { font-size: 12px; color: var(--ink-body); margin-top: 2px; }

  .contact {
    position: absolute; left: 135px; top: 262px;
    font-size: 13px; color: var(--ink-body); line-height: 19px;
  }
  .contact__row { display: flex; align-items: center; gap: 8px; }
  .contact__row--indent { padding-left: 20px; }
  .contact__icon { width: 12px; height: 12px; flex: none; }
  .contact__row--email { padding-left: 20px; margin-top: 4px; }

  .back-panel {
    position: absolute; left: 44px; top: 36px; right: 44px; bottom: 36px;
    background: var(--panel-gray);
    display: flex; align-items: center; justify-content: center;
  }
  .back-wordmark {
    font-family: "Oswald", sans-serif; font-weight: 600;
    font-size: 54px; color: var(--brand-green); letter-spacing: 1px;
    text-transform: uppercase;
  }
</style>
</head>
<body>

  <section class="card card--front" aria-label="Business card front">
    <div class="side-band"></div>
    <div class="accent-green"></div>
    <div class="accent-gray"></div>
    <div class="corner-block"></div>
    <div class="green-band"></div>

    <div class="person">
      <div class="person__name">Your Name</div>
      <div class="person__title">Title</div>
    </div>

    <h1 class="company-name">Dentworks Garage</h1>

    <div class="contact">
      <div class="contact__row">
        <svg class="contact__icon" viewBox="0 0 12 12" aria-hidden="true">
          <path d="M6 0.5a4 4 0 0 0-4 4c0 3 4 7 4 7s4-4 4-7a4 4 0 0 0-4-4zm0 5.5a1.5 1.5 0 1 1 0-3 1.5 1.5 0 0 1 0 3z" fill="#444"/>
        </svg>
        <span>XYZ ,XYZ Street , Address in Full</span>
      </div>
      <div class="contact__row">
        <svg class="contact__icon" viewBox="0 0 12 12" aria-hidden="true">
          <circle cx="6" cy="6" r="5.3" fill="none" stroke="#444" stroke-width="1"/>
          <path d="M4 3.2l1 1.3-.6.8c.4.8 1 1.4 1.8 1.8l.8-.6 1.3 1-.6 1c-2 0-4.4-2.4-4.4-4.4z" fill="#444"/>
        </svg>
        <span>+011-1234-567</span>
      </div>
      <div class="contact__row contact__row--indent"><span>+022-1234-567</span></div>
      <div class="contact__row contact__row--email"><span>username@website.com</span></div>
    </div>
  </section>

  <section class="card card--back" aria-label="Business card back">
    <div class="back-panel">
      <div class="back-wordmark">Dentworks Garage</div>
    </div>
  </section>

</body>
</html>
```